Business Card Design Project

double sided, embossed, name & logo on front font sonsie one, back Name Maribel Stoddart, mobile 0468214093, Phone 76139584,
email maribel@brightwipe.com, use sysbols on the back for example an envelope for email, a telephone for phone number etc.symbol slate grey writing navy blue

Industry/Entity Type

Business

```html
<!DOCTYPE html>
<html lang="en">
<head>
<meta charset="utf-8">
<title>Bright Wipe – Business Card</title>
<link href="https://fonts.googleapis.com/css2?family=Sonsie+One&family=Open+Sans:wght@400&display=swap" rel="stylesheet">
<style>
  :root {
    --page-bg: #e9ecef;
    --front-deep: #0f2fc2;
    --front-light: #6f90ff;
    --front-name: #5a78ea;
    --back-blue: #1a3fd6;
    --back-white: #ffffff;
    --navy: #0b1f8f;
    --slate: #6b7a8c;
    --faint-name: #a9b6e0;
  }
  * { margin: 0; padding: 0; box-sizing: border-box; }
  html, body {
    width: 1200px; height: 853px; overflow: hidden;
    background: var(--page-bg);
  }
  .canvas { position: relative; width: 1200px; height: 853px; }
  .card {
    position: absolute; left: 320px;
    width: 560px; height: 320px;
    box-shadow: 0 6px 18px rgba(0,0,0,0.25);
    overflow: hidden;
  }
  .card--front {
    top: 74px;
    background:
      radial-gradient(ellipse 60% 70% at 72% 30%, var(--front-light) 0%, rgba(111,144,255,0) 70%),
      linear-gradient(135deg, var(--front-deep) 0%, #1a3bd0 60%, #1230c0 100%);
  }
  .front-brand {
    position: absolute; left: 70px; top: 134px;
    font-family: "Open Sans", sans-serif;
    font-weight: 400; font-size: 40px; line-height: 52px;
    color: var(--front-name);
  }
  .card--back {
    top: 459px;
    background:
      radial-gradient(ellipse 55% 75% at 22% 30%, var(--back-blue) 0%, rgba(26,63,214,0.55) 35%, rgba(255,255,255,0) 75%),
      linear-gradient(115deg, #7d95ec 0%, var(--back-white) 62%);
  }
  .back-brand {
    position: absolute; left: 250px; top: 62px;
    font-family: "Open Sans", sans-serif;
    font-weight: 400; font-size: 30px; line-height: 40px;
    color: var(--faint-name);
  }
  .contact {
    position: absolute; left: 118px; top: 175px;
    color: var(--navy);
  }
  .contact__name {
    font-family: "Sonsie One", cursive;
    font-size: 16px; line-height: 22px; margin-bottom: 6px;
  }
  .contact__line {
    display: flex; align-items: center; gap: 6px;
    font-family: "Open Sans", sans-serif;
    font-size: 15px; line-height: 23px;
  }
  .contact__icon { width: 11px; height: 11px; flex: none; }
  .contact__icon * { fill: none; stroke: var(--slate); stroke-width: 1.4; }
  .contact__icon .solid { fill: var(--slate); stroke: none; }
</style>
</head>
<body>
<main class="canvas">
  <section class="card card--front" aria-label="Card front">
    <div class="front-brand">Bright Wipe</div>
  </section>

  <section class="card card--back" aria-label="Card back">
    <div class="back-brand">Bright Wipe</div>
    <div class="contact">
      <div class="contact__name">Maribel Stoddart</div>
      <div class="contact__line">
        <svg class="contact__icon" viewBox="0 0 12 12" aria-hidden="true">
          <rect x="3" y="0.8" width="6" height="10.4" rx="1"/>
          <rect class="solid" x="5" y="9" width="2" height="1"/>
        </svg>
        <span>0468214093</span>
      </div>
      <div class="contact__line">
        <svg class="contact__icon" viewBox="0 0 12 12" aria-hidden="true">
          <path class="solid" d="M2.5 1 L4.5 1 L5.3 3.6 L4 4.6 C4.7 6.1 5.9 7.3 7.4 8 L8.4 6.7 L11 7.5 L11 9.5 C11 10.4 10.3 11 9.5 11 C5.2 10.6 1.4 6.8 1 2.5 C1 1.7 1.6 1 2.5 1 Z"/>
        </svg>
        <span>76139584</span>
      </div>
      <div class="contact__line">
        <svg class="contact__icon" viewBox="0 0 12 12" aria-hidden="true">
          <rect x="0.8" y="2.2" width="10.4" height="7.6"/>
          <path d="M0.8 2.2 L6 6.6 L11.2 2.2"/>
        </svg>
        <span>maribel@brightwipe.com</span>
      </div>
    </div>
  </section>
</main>
</body>
</html>
```